Tail Meadow Website Design

Need a website for a Dog Grooiming business. Please make it simular to these:

https://www.wagtrolley.com
https://plainhaulo.com
https://thenookforkin.com
https://www.velmoro.com/portal/

```html
<!DOCTYPE html>
<html lang="en">
<head>
<meta charset="utf-8">
<title>Tail Meadow – Doorstep Dog Grooming</title>
<link rel="stylesheet" href="https://fonts.googleapis.com/css2?family=Montserrat:wght@500;600;700;800&family=Roboto+Condensed:wght@400;700&family=Nunito+Sans:ital,wght@0,400;0,600;0,700;1,400&display=swap">
<style>
:root{
  --blue:#1e90ff;
  --blue-light:#55b4ff;
  --blue-deep:#0f4f9c;
  --navy:#0c3a7a;
  --green:#2db55d;
  --green-light:#5ee07e;
  --green-dark:#1f8f3f;
  --ink:#333d48;
  --muted:#6b7480;
  --line:#e4e7ea;
  --white:#ffffff;
  --footer:#f7f9fb;
}
*{box-sizing:border-box;margin:0;padding:0}
html,body{width:1200px;height:3830px;overflow:hidden}
body{position:relative;background:var(--white);font-family:"Nunito Sans",Arial,sans-serif;color:var(--ink)}
.abs{position:absolute}

/* header */
.site-header{left:0;top:0;width:1200px;height:92px;background:var(--white);border-bottom:1px solid var(--line);z-index:5}
.brand{left:128px;top:22px;font-family:"Montserrat",sans-serif;font-weight:700;font-size:30px;color:var(--blue);letter-spacing:-.5px}
.main-nav{left:352px;top:36px;display:flex;gap:48px;font-family:"Roboto Condensed",sans-serif;font-size:15px;color:#222}
.main-nav a{color:inherit;text-decoration:none;position:relative}
.main-nav a.active::after{content:"";position:absolute;left:0;right:0;top:26px;height:3px;background:var(--green)}
.call-pill{left:870px;top:25px;width:201px;height:40px;border-radius:20px;background:var(--blue);color:var(--white);font-family:"Roboto Condensed",sans-serif;font-size:15px;display:flex;align-items:center;justify-content:center;gap:5px}
.call-pill b{font-weight:700}

/* hero */
.hero{left:0;top:92px;width:1200px;height:710px;overflow:hidden}
.hero-photo{left:0;top:0;width:1200px;height:710px;background:linear-gradient(100deg,#f3f1ee 0%,#ebe7e2 40%,#c79a63 62%,#8a6a4a 78%,#2b2b2e 92%)}
.hero-arrow{top:288px;width:30px;height:50px}
.hero-ring{left:80px;top:105px;width:494px;height:494px;border-radius:50%;border:1.5px solid #7a8a95}
.hero-disc{left:104px;top:127px;width:446px;height:446px;border-radius:50%;background:linear-gradient(150deg,var(--green-light) 0%,var(--green) 55%,#23a04c 100%);box-shadow:0 10px 30px rgba(0,0,0,.15)}
.hero-copy{left:104px;top:240px;width:446px;text-align:center;color:var(--white)}
.hero-copy h1{font-family:"Montserrat",sans-serif;font-weight:700;font-size:50px;line-height:54px}
.hero-copy p{margin-top:14px;font-size:18px;line-height:28px;padding:0 60px}
.btn{display:inline-flex;align-items:center;justify-content:center;border-radius:26px;font-family:"Roboto Condensed",sans-serif;font-weight:700;letter-spacing:1.2px;font-size:15px;text-decoration:none}
.btn-dark{background:#166b33;color:var(--white)}
.hero-copy .btn{margin-top:22px;width:183px;height:48px;font-size:16px}

/* about */
.about{left:0;top:798px;width:1200px;height:536px;background:linear-gradient(100deg,var(--blue) 0%,#3aa2ff 60%,var(--blue-light) 100%)}
.hero-curve{left:0;top:600px;width:1200px;height:200px;z-index:2}
.about-media{left:74px;top:85px;width:560px;height:478px;border-radius:24px;background:linear-gradient(150deg,#f4f6f8 0%,#dfe4e8 55%,#c9a57a 100%);z-index:3}
.about-copy{left:666px;top:112px;width:460px;color:var(--white)}
.about-copy h2{font-family:"Montserrat",sans-serif;font-weight:700;font-size:32px}
.about-copy p{margin-top:22px;font-size:16px;line-height:25px}
.about-actions{margin-top:34px;display:flex;gap:6px}
.btn-blue{background:var(--blue);color:var(--white);width:168px;height:44px;box-shadow:0 4px 12px rgba(0,60,140,.25)}
.btn-ghost{border:2px solid var(--white);color:var(--white);width:168px;height:44px}
.btn svg{margin-right:6px}
.about-tail{left:0;top:1332px;width:260px;height:160px;z-index:1}

/* services */
.section-title{font-family:"Montserrat",sans-serif;font-weight:700;font-size:34px;color:var(--navy)}
.section-title em{font-style:normal;color:var(--green)}
.services-title{left:0;top:1404px;width:1200px;text-align:center}
.service-card{top:1523px;width:226px;height:224px;border:2px solid #6fcf8c;text-align:center;padding:68px 18px 0}
.service-card h3{font-family:"Montserrat",sans-serif;font-weight:700;font-size:14px;color:var(--navy);line-height:20px}
.service-card p{margin-top:12px;font-size:12.5px;line-height:17px;color:var(--muted)}
.service-icon{top:1480px;width:86px;height:86px;border-radius:50%;display:flex;align-items:center;justify-content:center;border:3px solid var(--white);box-shadow:0 3px 8px rgba(0,0,0,.12)}

/* why */
.why{left:0;top:1850px;width:1200px;height:532px;overflow:hidden}
.why-photo{left:0;top:0;width:620px;height:532px;background:linear-gradient(120deg,#f2f2f4 0%,#e6e1dc 45%,#c59c74 70%,#c9a2a8 100%)}
.why-shape{left:0;top:0;width:1200px;height:532px}
.why-copy{left:687px;top:108px;width:420px;color:var(--white)}
.why-copy h2{font-family:"Montserrat",sans-serif;font-weight:700;font-size:32px}
.why-copy p{margin-top:16px;font-size:13px;line-height:21px}
.perk{display:flex;align-items:center;gap:12px;font-family:"Montserrat",sans-serif;font-weight:600;font-size:14px;line-height:17px;color:var(--white)}
.perk-icon{width:70px;height:70px;border-radius:50%;background:var(--white);display:flex;align-items:center;justify-content:center;flex:none}

/* testimonials */
.reviews-title{left:119px;top:2484px}
.review{top:2558px;width:314px;height:228px;border:2px solid #dfe3e6;border-radius:4px;padding:30px 36px 0}
.review p{font-style:italic;font-size:12.5px;line-height:18px;color:#5a6470}
.reviewer{margin-top:14px;display:flex;align-items:center;gap:10px}
.avatar{width:36px;height:36px;border-radius:50%;background:linear-gradient(160deg,#e9c3a3,#b07a5a)}
.reviewer b{display:block;font-family:"Montserrat",sans-serif;font-size:11px;color:var(--navy)}
.stars{color:#f5a623;font-size:17px;letter-spacing:1px;line-height:18px}
.reviews-photo{left:796px;top:2418px;width:290px;height:462px;border-radius:140px 140px 0 0;background:linear-gradient(170deg,#f1c27a 0%,#d8933f 55%,#b8702b 100%)}

/* booking */
.booking{left:0;top:2879px;width:1200px;height:568px;background:linear-gradient(180deg,var(--blue) 0%,#3ea6ff 100%);overflow:hidden}
.skyline{left:0;top:120px;width:1200px;height:448px;background:linear-gradient(180deg,rgba(255,255,255,0) 0%,rgba(10,90,200,.22) 60%,rgba(10,90,200,.3) 100%)}
.booking h2{position:absolute;left:0;top:72px;width:1200px;text-align:center;font-family:"Montserrat",sans-serif;font-weight:700;font-size:34px;color:var(--white)}
.booking p{position:absolute;left:260px;top:124px;width:680px;text-align:center;font-size:14px;line-height:22px;color:var(--white)}
.booking-actions{left:0;top:182px;width:1200px;display:flex;justify-content:center;gap:6px}
.btn-green{background:var(--green);color:var(--white);width:168px;height:44px}
.btn-navy{background:var(--navy);color:var(--white);width:168px;height:44px}
.booking-photo{left:305px;top:250px;width:602px;height:318px;border-radius:160px 160px 0 0;background:linear-gradient(90deg,#ef5fb0 0%,#b9743f 35%,#29a6e8 55%,#f7f3ee 72%,#f6c531 100%)}

/* footer */
.site-footer{left:0;top:3447px;width:1200px;height:383px;background:var(--footer)}
.foot-head{font-family:"Montserrat",sans-serif;font-weight:600;font-size:15px;color:var(--navy);padding-bottom:6px;position:relative}
.foot-head::after{content:"";position:absolute;left:0;bottom:0;width:40px;height:2px;background:var(--green)}
.foot-links{list-style:none;font-size:12.5px;color:var(--muted);line-height:26px}
.contact-row{display:flex;gap:12px;margin-top:14px}
.contact-row b{display:block;font-family:"Montserrat",sans-serif;font-size:12px;color:var(--navy)}
.contact-row span{font-size:12.5px;color:var(--muted);line-height:21px}
.social{left:178px;top:268px;display:flex;gap:8px}
.social i{width:24px;height:24px;border-radius:50%;background:var(--navy);display:block}
.foot-rule{left:0;top:330px;width:1200px;height:1px;background:var(--line)}
.copyright{left:0;top:344px;width:1200px;text-align:center;font-size:11px;color:var(--muted)}
</style>
</head>
<body>

<header class="site-header abs">
  <div class="brand abs">Tail Meadow</div>
  <nav class="main-nav abs">
    <a class="active" href="#">ABOUT US</a><a href="#">SERVICES</a><a href="#">TESTIMONIALS</a><a href="#">BLOGS</a><a href="#">CONTACT</a>
  </nav>
  <div class="call-pill abs">CALL US <b>(555) 014-2290</b></div>
</header>

<section class="hero abs">
  <div class="hero-photo abs" role="img" aria-label="Groomer combing a small long-haired terrier with a bow in its topknot"></div>
  <svg class="hero-arrow abs" style="left:32px" viewBox="0 0 30 50"><path d="M24 4 L6 25 L24 46" fill="none" stroke="#9aa3aa" stroke-width="3"/></svg>
  <svg class="hero-arrow abs" style="left:1140px" viewBox="0 0 30 50"><path d="M6 4 L24 25 L6 46" fill="none" stroke="#ffffff" stroke-width="3" opacity=".8"/></svg>
  <div class="hero-ring abs"></div>
  <div class="hero-disc abs"></div>
  <div class="hero-copy abs">
    <h1>Doorstep Dog Grooming</h1>
    <p>Lorem ipsum dolor sit amet, consectetur adipscing elit, sed</p>
    <a class="btn btn-dark" href="#">BOOK NOW</a>
  </div>
</section>

<svg class="hero-curve abs" viewBox="0 0 1200 200" preserveAspectRatio="none">
  <path d="M600 200 C900 196 1120 150 1200 8 L1200 200 Z" fill="#4aaeff"/>
</svg>

<section class="about abs">
  <div class="about-media abs" role="img" aria-label="White grooming van with two bulldog puppies in a wooden tub beside shampoo bottles and towels"></div>
  <div class="about-copy abs">
    <h2>About Tail Meadow</h2>
    <p>Lorem ipsum dolor sit amet, consectetur adipiscing elit, sed do eiusmod tempor incididunt ut labore et dolor</p>
    <p>Ut enim ad minim veniam, quis nostrud exercitation ullamco laboris nisi ut aliquip ex ea commodo consequat. Duis aute irure dolor in reprehenderi.</p>
    <div class="about-actions">
      <a class="btn btn-blue" href="#">LEARN MORE</a>
      <a class="btn btn-ghost" href="#"><svg width="14" height="14" viewBox="0 0 24 24"><path d="M6.6 10.8a15.1 15.1 0 0 0 6.6 6.6l2.2-2.2c.3-.3.7-.4 1-.2 1.1.4 2.3.6 3.6.6.6 0 1 .4 1 1V20c0 .6-.4 1-1 1A17 17 0 0 1 3 4c0-.6.4-1 1-1h3.5c.6 0 1 .4 1 1 0 1.3.2 2.5.6 3.6.1.3 0 .7-.2 1z" fill="#fff"/></svg>CALL US</a>
    </div>
  </div>
</section>
<svg class="about-tail abs" viewBox="0 0 260 160"><path d="M0 0 L260 0 C120 8 20 60 0 160 Z" fill="#1e90ff"/></svg>

<h2 class="section-title services-title abs">Our <em>Services</em></h2>

<div class="service-card abs" style="left:128px"><h3>Bath with Shampoo<br>and Conditioner</h3><p>Lorem ipsum dolor sit amet, consectetur adipiscing elit. Ut elit tellus, luctus nec ullamcorp</p></div>
<div class="service-card abs" style="left:364px"><h3>Full Body Trimming<br>and Styling</h3><p>Lorem ipsum dolor sit amet, consectetur adipiscing elit. Ut elit tellus, luctus nec ullamcorp</p></div>
<div class="service-card abs" style="left:602px"><h3>Eyes &amp; Ears<br>Cleaning</h3><p>Lorem ipsum dolor sit amet, consectetur adipiscing elit. Ut elit tellus, luctus nec ullamcorp</p></div>
<div class="service-card abs" style="left:842px"><h3>Breed Specific Pro<br>Grooming</h3><p>Lorem ipsum dolor sit amet, consectetur adipiscing elit. Ut elit tellus, luctus nec ullamcorp</p></div>

<div class="service-icon abs" style="left:198px;background:var(--green)"><svg width="44" height="44" viewBox="0 0 44 44" fill="none" stroke="#fff" stroke-width="2"><path d="M8 26h28v4a8 8 0 0 1-8 8H16a8 8 0 0 1-8-8z"/><circle cx="22" cy="16" r="6"/><circle cx="14" cy="8" r="2"/><circle cx="30" cy="7" r="2"/></svg></div>
<div class="service-icon abs" style="left:434px;background:var(--navy)"><svg width="44" height="44" viewBox="0 0 44 44" fill="none" stroke="#fff" stroke-width="2"><circle cx="11" cy="12" r="4"/><circle cx="11" cy="24" r="4"/><path d="M14 14l16 6M14 22l16-6"/><path d="M20 36c0-6 4-8 8-8s8 2 8 8z"/></svg></div>
<div class="service-icon abs" style="left:672px;background:var(--blue)"><svg width="44" height="44" viewBox="0 0 44 44" fill="none" stroke="#fff" stroke-width="2"><path d="M10 10l6 4h12l6-4-2 14c0 8-5 12-10 12s-10-4-10-12z"/><circle cx="18" cy="22" r="1.5" fill="#fff"/><circle cx="26" cy="22" r="1.5" fill="#fff"/></svg></div>
<div class="service-icon abs" style="left:912px;background:var(--blue-light)"><svg width="44" height="44" viewBox="0 0 44 44" fill="none" stroke="#fff" stroke-width="2"><circle cx="20" cy="24" r="10"/><circle cx="20" cy="24" r="4"/><path d="M28 14l8-8M32 6h4v4"/></svg></div>

<section class="why abs">
  <div class="why-photo abs" role="img" aria-label="Groomer holding the paw of a small terrier to trim its nails"></div>
  <svg class="why-shape abs" viewBox="0 0 1200 532" preserveAspectRatio="none">
    <path d="M540 0 C610 170 590 380 440 532 L470 532 C620 380 640 170 570 0 Z" fill="#1e90ff"/>
    <path d="M570 0 L1200 0 L1200 532 L470 532 C620 380 640 170 570 0 Z" fill="url(#whyGrad)"/>
    <defs><linearGradient id="whyGrad" x1="0" y1="0" x2="1" y2="1"><stop offset="0" stop-color="#2aab47"/><stop offset="1" stop-color="#35bf5c"/></linearGradient></defs>
  </svg>
  <div class="why-copy abs">
    <h2>Why Tail Meadow</h2>
    <p>Lorem ipsum dolor sit amet, consectetur adipiscing elit, sed do eiusmod tempor incididunt ut labore et dolore.</p>
  </div>
  <div class="perk abs" style="left:686px;top:234px"><span class="perk-icon"><svg width="34" height="34" viewBox="0 0 34 34" fill="none" stroke="#1e90ff" stroke-width="2"><path d="M17 4c6 8 9 12 9 17a9 9 0 0 1-18 0c0-5 3-9 9-17z"/></svg></span>WARM<br>WATER BATH</div>
  <div class="perk abs" style="left:904px;top:234px"><span class="perk-icon"><svg width="34" height="34" viewBox="0 0 34 34" fill="none" stroke="#1e90ff" stroke-width="2"><path d="M6 28l14-14M18 8l8 8 4-4-8-8z"/></svg></span>GENTLE BRUSH<br>AND BLOWOUT</div>
  <div class="perk abs" style="left:686px;top:336px"><span class="perk-icon"><svg width="34" height="34" viewBox="0 0 34 34" fill="none" stroke="#1e90ff" stroke-width="2"><rect x="10" y="12" width="14" height="18" rx="3"/><path d="M14 12V7h6v5M20 7h5"/></svg></span>ALL NATURAL<br>PRODUCTS</div>
  <div class="perk abs" style="left:904px;top:336px"><span class="perk-icon"><svg width="34" height="34" viewBox="0 0 34 34" fill="none" stroke="#1e90ff" stroke-width="2"><circle cx="11" cy="9" r="4"/><circle cx="20" cy="9" r="4"/><path d="M13 13l5 17M18 13l-5 17"/></svg></span>TRIM &amp;<br>FILE NAILS</div>
</section>

<h2 class="section-title reviews-title abs">What <em>Our Customer Says</em></h2>
<div class="review abs" style="left:120px">
  <p>Lorem ipsum dolor sit amet, consectetur adipiscing elit, sed do eiusmod tempor incididunt ut labore et dolore magna aliqua. Ut enim ad minim veniam, quis nostrud exercitation ullamco laboris nisi ut aliquieus mod tempor incididunt ut labore</p>
  <div class="reviewer"><span class="avatar" role="img" aria-label="Customer portrait"></span><div><b>Marla Quenby</b><span class="stars">★★★★★</span></div></div>
</div>
<div class="review abs" style="left:455px">
  <p>Lorem ipsum dolor sit amet, consectetur adipiscing elit, sed do eiusmod tempor incididunt ut labore et dolore magna aliqua. Ut enim ad minim veniam, quis nostrud exercitation ullamco laboris nisi ut aliquieus mod tempor incididunt ut labore</p>
  <div class="reviewer"><span class="avatar" role="img" aria-label="Customer portrait"></span><div><b>Marla Quenby</b><span class="stars">★★★★★</span></div></div>
</div>
<div class="reviews-photo abs" role="img" aria-label="Golden retriever sitting and smiling"></div>

<section class="booking abs">
  <div class="skyline abs" role="img" aria-label="Faint city skyline silhouette in blue"></div>
  <h2>Book Onlie Grooming Service</h2>
  <p>Lorem ipsum dolor sit amet, consectetur adipiscing elit, sed do eiusmod tempor incididunt ut labore et dolore.Lorem ipsum dolor sit amet, consectetur adipiscing elit, sed do eiusmod</p>
  <div class="booking-actions abs">
    <a class="btn btn-green" href="#">LEARN MORE</a>
    <a class="btn btn-navy" href="#"><svg width="14" height="14" viewBox="0 0 24 24"><path d="M6.6 10.8a15.1 15.1 0 0 0 6.6 6.6l2.2-2.2c.3-.3.7-.4 1-.2 1.1.4 2.3.6 3.6.6.6 0 1 .4 1 1V20c0 .6-.4 1-1 1A17 17 0 0 1 3 4c0-.6.4-1 1-1h3.5c.6 0 1 .4 1 1 0 1.3.2 2.5.6 3.6.1.3 0 .7-.2 1z" fill="#fff"/></svg>CALL US</a>
  </div>
  <div class="booking-photo abs" role="img" aria-label="Three small dogs wrapped in pink, blue and yellow towels"></div>
</section>

<footer class="site-footer abs">
  <div class="abs" style="left:170px;top:86px;width:300px">
    <h4 class="foot-head">NAVIGATION</h4>
    <div style="display:flex;gap:56px;margin-top:12px">
      <ul class="foot-links"><li>Home</li><li>About Us</li><li>Grooming Services</li><li>Why We Are</li></ul>
      <ul class="foot-links"><li>Testimonials</li><li>Book Online Now</li><li>Blogs</li><li>Contact Us</li></ul>
    </div>
  </div>
  <div class="social abs"><i></i><i></i><i></i></div>
  <div class="abs" style="left:535px;top:88px;width:220px">
    <h4 class="foot-head">LOCATION WE SERVE</h4>
    <ul class="foot-links" style="margin-top:12px"><li>Lorem ipsum dolor</li><li>Sit amet consectetur</li><li>Adipiscing elit</li><li>Eed do eiusmod</li><li>Tempor</li></ul>
  </div>
  <div class="abs" style="left:826px;top:86px;width:260px">
    <h4 class="foot-head">CONTACT US</h4>
    <div class="contact-row"><svg width="30" height="30" viewBox="0 0 24 24" fill="none" stroke="#0c3a7a" stroke-width="1.5"><path d="M6.6 10.8a15.1 15.1 0 0 0 6.6 6.6l2.2-2.2c.3-.3.7-.4 1-.2 1.1.4 2.3.6 3.6.6.6 0 1 .4 1 1V20c0 .6-.4 1-1 1A17 17 0 0 1 3 4c0-.6.4-1 1-1h3.5c.6 0 1 .4 1 1 0 1.3.2 2.5.6 3.6.1.3 0 .7-.2 1z"/></svg><div><b>PHONE NUMBER</b><span>(555) 014-2290</span></div></div>
    <div class="contact-row" style="margin-top:22px"><svg width="30" height="30" viewBox="0 0 24 24" fill="none" stroke="#0c3a7a" stroke-width="1.5"><circle cx="12" cy="12" r="9"/><path d="M8 12l3 3 6-7"/></svg><div><b>WORKING HOURS</b><span>Mon- Fri: 7:00 Am to 9:00 Pm<br>Sat-Sun: 8:00 Am to 5:00 Pm</span></div></div>
  </div>
  <div class="foot-rule abs"></div>
  <div class="copyright abs">© 2020 Tail Meadow All Rights Reserved.</div>
</footer>

</body>
</html>
```